Stationery Design needed for logo design project

This project is linked to Tiravo Nusa Kencana.

Our company needs a Stationery Design. Please refer to our original project in the link above.

Reason: The logo just finished ...

```html
<!DOCTYPE html>
<html lang="en">
<head>
<meta charset="utf-8">
<title>Tiravo Nusa Kencana Stationery</title>
<link rel="stylesheet" href="https://fonts.googleapis.com/css2?family=Quicksand:wght@400;500;600&display=swap">
<style>
  :root {
    --backdrop: #e8e8e8;
    --ink: #231f20;
    --ink-deep: #1a1718;
    --paper: #f4f4f4;
    --line-grey: #8c8c8c;
    --text-light: #cfcfcf;
    --text-dark: #3a3a3a;
    --shadow: 0 2px 6px rgba(0,0,0,0.18);
  }
  * { margin: 0; padding: 0; box-sizing: border-box; }
  html, body { width: 1200px; height: 900px; overflow: hidden; }
  body {
    background: radial-gradient(ellipse at 50% 40%, #f3f3f3 0%, var(--backdrop) 70%);
    font-family: "Quicksand", sans-serif;
    position: relative;
  }
  .piece { position: absolute; box-shadow: var(--shadow); overflow: hidden; }
  .piece svg.arc { position: absolute; left: 0; top: 0; }
  .dark { background: var(--ink); color: var(--text-light); }
  .light { background: var(--paper); color: var(--text-dark); }

  .brand { display: flex; align-items: center; gap: 6px; font-weight: 600; white-space: nowrap; letter-spacing: 0.02em; }
  .brand-dot { border-radius: 50%; flex: none; }
  .dark .brand { color: #ffffff; }
  .dark .brand-dot { background: #ffffff; }
  .light .brand { color: var(--ink); }
  .light .brand-dot { background: var(--ink); }

  .figure-area {
    position: absolute;
    background: radial-gradient(ellipse at center, rgba(140,140,140,0.16) 0%, rgba(140,140,140,0) 70%);
  }

  /* folder */
  .folder { left: 88px; top: 265px; width: 345px; height: 472px; }
  .folder .figure-area { left: 130px; top: 250px; width: 215px; height: 222px; }

  /* letterhead */
  .letterhead { left: 457px; top: 289px; width: 315px; height: 445px; }
  .letterhead .brand { position: absolute; right: 30px; top: 36px; font-size: 13px; }
  .letterhead .brand-dot { width: 12px; height: 12px; }
  .letterhead .contact { position: absolute; right: 32px; top: 60px; font-size: 4px; line-height: 6.4px; text-align: right; }
  .letterhead .figure-area { left: 0; top: 290px; width: 175px; height: 155px; }

  /* envelopes */
  .envelope-front { left: 797px; top: 217px; width: 329px; height: 164px; }
  .envelope-front .brand { position: absolute; left: 18px; top: 76px; font-size: 15px; }
  .envelope-front .brand-dot { width: 14px; height: 14px; }
  .envelope-front .web { position: absolute; left: 50px; top: 150px; font-size: 5px; color: #8a8a8a; }

  .envelope-back { left: 797px; top: 389px; width: 329px; height: 164px; }
  .envelope-back .flap { position: absolute; left: 0; top: 0; }
  .envelope-back .contact { position: absolute; left: 22px; top: 100px; font-size: 4.6px; line-height: 7px; }
  .envelope-back .contact span { display: flex; align-items: center; gap: 3px; }
  .envelope-back .figure-area { left: 210px; top: 50px; width: 119px; height: 114px; }

  /* business cards */
  .card-front { left: 815px; top: 585px; width: 110px; height: 66px; }
  .card-front .brand { position: absolute; left: 14px; top: 10px; font-size: 6px; gap: 3px; }
  .card-front .brand-dot { width: 6px; height: 6px; }
  .card-front .contact { position: absolute; left: 14px; top: 28px; font-size: 2.6px; line-height: 4.2px; color: #9a9a9a; }
  .card-front .holder { position: absolute; right: 8px; top: 32px; text-align: right; }
  .card-front .holder-name { font-size: 6px; font-weight: 500; color: #ffffff; }
  .card-front .holder-role { font-size: 2.6px; color: #9a9a9a; }

  .card-back { left: 963px; top: 585px; width: 134px; height: 66px; }
  .card-back .figure-area { left: 80px; top: 20px; width: 54px; height: 46px; }
</style>
</head>
<body>

  <section class="piece dark folder">
    <svg class="arc" width="345" height="472" viewBox="0 0 345 472" aria-hidden="true">
      <circle cx="72" cy="0" r="106" fill="none" stroke="var(--line-grey)" stroke-width="4"/>
    </svg>
    <div class="figure-area" role="img" aria-label="Brand line figure decoration"></div>
  </section>

  <section class="piece light letterhead">
    <div class="brand"><span class="brand-dot"></span>tiravo nusa kencana</div>
    <address class="contact" style="font-style:normal">
      Arvena Tower, 5th Floor<br>
      Jl. Melati Raya No. 14<br>
      Jakarta Selatan, 12950<br>
      +62 800 555 0142<br>
      +62 21 5550 1930<br>
      +62 21 5550 1931<br>
      www.tiravonusa.com
    </address>
    <div class="figure-area" role="img" aria-label="Brand line figure decoration"></div>
  </section>

  <section class="piece dark envelope-front">
    <div class="brand"><span class="brand-dot"></span>tiravo nusa kencana</div>
    <div class="web">www.tiravonusa.com</div>
  </section>

  <section class="piece dark envelope-back">
    <svg class="flap" width="329" height="164" viewBox="0 0 329 164" aria-hidden="true">
      <polygon points="0,0 329,0 312,22 17,22" fill="var(--ink-deep)"/>
    </svg>
    <address class="contact" style="font-style:normal">
      <span><svg width="5" height="5" viewBox="0 0 10 10"><path d="M5 1a3 3 0 0 1 3 3c0 2.2-3 5-3 5S2 6.2 2 4a3 3 0 0 1 3-3z" fill="none" stroke="currentColor"/></svg>Arvena Tower, 5th Floor</span>
      <span style="padding-left:8px">Jl. Melati Raya No. 14</span>
      <span style="padding-left:8px">Jakarta Selatan, 12950</span>
      <span><svg width="5" height="5" viewBox="0 0 10 10"><rect x="2.5" y="1" width="5" height="8" rx="1" fill="none" stroke="currentColor"/></svg>+62 800 555 0142</span>
      <span><svg width="5" height="5" viewBox="0 0 10 10"><path d="M2 2l2 0 1 2-1 1a5 5 0 0 0 2 2l1-1 2 1 0 2c-4 0-7-3-7-7z" fill="currentColor"/></svg>+62 21 5550 1930</span>
      <span><svg width="5" height="5" viewBox="0 0 10 10"><rect x="1" y="2" width="8" height="6" fill="none" stroke="currentColor"/></svg>+62 21 5550 1931</span>
      <span><svg width="5" height="5" viewBox="0 0 10 10"><circle cx="5" cy="5" r="4" fill="none" stroke="currentColor"/></svg>www.tiravonusa.com</span>
    </address>
    <div class="figure-area" role="img" aria-label="Brand line figure decoration"></div>
  </section>

  <section class="piece dark card-front">
    <div class="brand"><span class="brand-dot"></span>tiravo nusa kencana</div>
    <address class="contact" style="font-style:normal">
      Arvena Tower, 5th Floor<br>
      Jakarta Selatan, 12950<br>
      +62 800 555 0142<br>
      +62 21 5550 1930<br>
      www.tiravonusa.com
    </address>
    <div class="holder">
      <div class="holder-name">dela safira</div>
      <div class="holder-role">Sales &amp; Marketing Director</div>
    </div>
  </section>

  <section class="piece dark card-back">
    <svg class="arc" width="134" height="66" viewBox="0 0 134 66" aria-hidden="true">
      <circle cx="22" cy="0" r="24" fill="none" stroke="var(--line-grey)" stroke-width="1.2"/>
    </svg>
    <div class="figure-area" role="img" aria-label="Brand line figure decoration"></div>
  </section>

</body>
</html>
```